Verdanix gym flyer

Use the text offered in the word document and add the appropriate images in the space provided. The images may need to be resized.Can the font be bold and silver with a black outline.Can the background be light blue.I have submitted a design request for some business cards. I'd like the cards and the flyer to match.

Industry/Entity Type

Gym

```html
<!DOCTYPE html>
<html lang="en">
<head>
<meta charset="utf-8">
<title>Verdanix Gym Flyer</title>
<link href="https://fonts.googleapis.com/css2?family=Cinzel:wght@700;900&family=Ubuntu:wght@500;700&display=swap" rel="stylesheet">
<style>
  :root {
    --bg-light: #c9f6ef;
    --bg-mid: #8fe3d6;
    --bg-deep: #6fd3c4;
    --silver: #d9dcde;
    --outline: #111111;
    --name-red: #7a0f12;
    --sub-grey: #4a4a4a;
    --white: #ffffff;
    --photo-frame: #fdfdfd;
  }
  * { margin: 0; padding: 0; box-sizing: border-box; }
  html, body { width: 1200px; height: 850px; overflow: hidden; }
  body { background: var(--bg-light); }
  .flyer {
    position: relative;
    width: 1200px; height: 850px;
    overflow: hidden;
    background:
      radial-gradient(ellipse at 50% 10%, rgba(255,255,255,0.75), rgba(255,255,255,0) 45%),
      radial-gradient(ellipse at 50% 95%, rgba(255,255,255,0.6), rgba(255,255,255,0) 40%),
      linear-gradient(180deg, var(--bg-light) 0%, var(--bg-mid) 55%, var(--bg-deep) 100%);
    font-family: 'Cinzel', serif;
  }
  .gym-backdrop {
    position: absolute; inset: 0;
    background: linear-gradient(160deg, rgba(255,255,255,0.15), rgba(90,180,170,0.2));
  }
  .headline, .tagline, .coach, .contact {
    position: absolute; left: 0; width: 100%;
    text-align: center;
    font-family: 'Cinzel', serif;
    font-weight: 900;
    font-variant: small-caps;
    color: var(--silver);
    -webkit-text-stroke: 3px var(--outline);
    paint-order: stroke fill;
    white-space: nowrap;
  }
  .headline { top: 34px; font-size: 37px; line-height: 42px; letter-spacing: 1px; }
  .tagline { top: 574px; font-size: 30px; line-height: 33px; letter-spacing: 0.5px; }
  .coach { top: 672px; font-size: 31px; line-height: 34px; letter-spacing: 0.5px; }
  .contact {
    top: 742px; font-size: 50px; line-height: 60px; letter-spacing: 2px;
    color: var(--white);
  }
  .photo-pair {
    position: absolute;
    background: var(--photo-frame);
    padding: 5px;
    display: flex; gap: 4px;
    box-shadow: 0 2px 8px rgba(0,0,0,0.15);
  }
  .photo-pair.left { left: 61px; top: 218px; width: 430px; height: 325px; transform: rotate(-9deg); }
  .photo-pair.right { left: 728px; top: 215px; width: 416px; height: 350px; transform: rotate(8deg); }
  .photo { flex: 1; }
  .photo.before-m { background: linear-gradient(160deg, #6f9d6a, #8a8d8f 60%, #3f5f3a); }
  .photo.after-m { background: linear-gradient(160deg, #f2f0ea, #d9a48a 55%, #2a2a2a); }
  .photo.before-f { background: linear-gradient(160deg, #bfc3c7, #2b2b2b 55%, #c49a85); }
  .photo.after-f { background: linear-gradient(160deg, #f3f1ec, #4a2f24 45%, #1c1c1c 80%); }
  .client { position: absolute; text-align: center; }
  .client.kerry { left: 546px; top: 192px; width: 340px; }
  .client.mark { left: 356px; top: 472px; width: 340px; }
  .client-name {
    font-family: 'Cinzel', serif; font-weight: 900;
    font-size: 36px; color: var(--name-red);
    font-variant: small-caps;
    letter-spacing: 1px;
    text-shadow: 0 0 3px #fff, 0 0 6px #fff, 0 0 10px #fff;
    line-height: 1.05;
  }
  .client-role, .client-age {
    font-family: 'Ubuntu', sans-serif; font-weight: 500;
    font-size: 26px; color: var(--sub-grey);
    text-shadow: 0 0 3px #fff, 0 0 6px #fff, 0 0 8px #fff;
    line-height: 1.0;
  }
</style>
</head>
<body>
<main class="flyer">
  <div class="gym-backdrop" role="img" aria-label="Faded photo of a gym with treadmills and exercise equipment"></div>

  <h1 class="headline">Are you happy with your body shape?<br>Would you like to improve your health &amp; energy levels<br>at the same time as transforming your body shape?</h1>

  <div class="photo-pair left">
    <div class="photo before-m" role="img" aria-label="Before photo of a man holding a bottle in a garden"></div>
    <div class="photo after-m" role="img" aria-label="After photo of the same man, slimmer and shirtless"></div>
  </div>

  <div class="photo-pair right">
    <div class="photo before-f" role="img" aria-label="Before photo of a woman in a black dress, seated"></div>
    <div class="photo after-f" role="img" aria-label="After photo of the same woman, slimmer, standing in a black dress"></div>
  </div>

  <div class="client kerry">
    <div class="client-name">Kerry Halston</div>
    <div class="client-role">Payroll Supervisor</div>
    <div class="client-age">Age 27</div>
  </div>

  <div class="client mark">
    <div class="client-name">Mark Danford</div>
    <div class="client-role">Retired Police Officer</div>
    <div class="client-age">Age 52</div>
  </div>

  <p class="tagline">Get your body looking exactly how you<br>want it to look and more importantly... KEEP IT THAT WAY</p>

  <p class="coach">Wellness &amp; Body Transformation Coach<br>Call Jamie for a FREE and unique body evaluation tailored to YOU.</p>

  <p class="contact">07700 900 482 SocialPage: Jamie Corwell</p>
</main>
</body>
</html>
```